9x12 Business Brochure, 3 fold, for Internet Marketing Company

I'd like to have a brochure designed for my Internet marketing company. I have the content all ready, 10 Internet Marketing Myths, which you can see here: http://www.brightfieldwebgrowth.net/usual-online-promo-fables/. I'm looking for something creative and business to business. The company is all about Internet marketing. I like the "http://" header I use at our website. People like it too and identify with it. Audience is business owners 35 to 55 years old. I use blue at my website. I *think* I would like the cover page (front page) to open with some attention grabbing text, that basically takes most of the front page of the brochure. It would probably say: "I Can Help You Get BETTER RESULTS from Your Website, More Traffic, TOP RANKINGS at Zorvix, More Leads and MORE SALES. But first you'll have to avoid these common Internet marketing myths..." The inside pages would have the content from above (the 10 myths). The back page would have testimonials that I can provide. And the inside folded in page (or what I call the inside folded in page) would have a list of services. I think I want the dimensions 12x9 which is a larger sized, three-fold brochure.

Target Market(s)

I use this brochure to send to business owners and managers to show them I know what I'm talking about and and expert. See attachment for content.

Industry/Entity Type

Marketing

Requirements
Should not have
• No clipart. Probably not illustrations. Photos. The "http://" used at the site is something people "connect" with and get that this is about Internet marketing.

```html
<!DOCTYPE html>
<html lang="en">
<head>
<meta charset="utf-8">
<title>Dana Whitlow Consulting – Tri-fold Brochure</title>
<link href="https://fonts.googleapis.com/css2?family=Roboto+Condensed:wght@400;700&family=PT+Sans:ital,wght@0,400;0,700;1,400&family=Arimo:wght@700&display=swap" rel="stylesheet">
<style>
  :root{
    --stage:#e9e9e9;
    --brand-blue:#4a8bc2;
    --band-blue:#3f86c4;
    --link-blue:#2f7bc0;
    --ink:#1a1a1a;
    --ink-soft:#333;
    --grey-text:#555;
    --quote-bar:rgba(40,40,40,.85);
    --pale-blue:#cfe0f0;
    --white:#fff;
  }
  *{box-sizing:border-box;margin:0;padding:0}
  html,body{width:1200px;height:924px;overflow:hidden;background:var(--stage)}
  .brochure{position:absolute;left:77px;top:63px;width:1032px;height:798px;display:flex;box-shadow:0 4px 14px rgba(0,0,0,.25)}
  .panel{position:relative;width:344px;height:100%;overflow:hidden}

  /* section band */
  .band{position:absolute;left:0;top:29px;width:300px;height:38px}
  .band svg{position:absolute;inset:0}
  .band h2{position:relative;font:700 23px/38px "Roboto Condensed",sans-serif;color:var(--white);padding-left:24px;letter-spacing:.2px}

  /* services panel */
  .panel--services{background:linear-gradient(180deg,#fafafa 0%,#eef3f8 45%,#d4e4f2 100%)}
  .services-art{position:absolute;left:0;top:300px;width:344px;height:498px;background:linear-gradient(160deg,rgba(255,255,255,0) 0%,rgba(160,195,225,.45) 55%,rgba(130,175,215,.6) 100%)}
  .service-list{position:absolute;left:26px;top:96px;list-style:none}
  .service-list li{position:relative;padding-left:23px;font:700 15.5px/28.7px "Arimo",sans-serif;color:var(--ink)}
  .service-list li::before{content:"";position:absolute;left:0;top:9px;width:11px;height:11px;border-radius:50%;background:#4d4d4d}
  .quote-bar{position:absolute;left:0;top:721px;width:336px;height:52px;background:var(--quote-bar);display:flex;align-items:center;justify-content:center;text-align:center}
  .quote-bar p{font:italic 400 15px/19px "PT Sans",sans-serif;color:var(--white)}

  /* stories panel */
  .panel--stories{background:linear-gradient(180deg,#ffffff 0%,#ffffff 62%,#dce9f5 82%,#b9d2ea 100%)}
  .stories{position:absolute;left:24px;top:92px;width:294px}
  .story{font:400 10.6px/13.4px "PT Sans",sans-serif;color:var(--ink-soft);text-align:justify;margin-bottom:10px}
  .story b{font:400 14.5px/13px "PT Sans",sans-serif;color:var(--link-blue)}
  .contact{position:absolute;left:0;width:344px;top:686px;text-align:center}
  .contact .name{font:700 18.5px/24px "PT Sans",sans-serif;color:var(--link-blue)}
  .contact .email{font:700 12.5px/20px "PT Sans",sans-serif;color:var(--ink-soft);letter-spacing:.3px;margin-top:2px}
  .contact .phone{font:700 16px/24px "Roboto Condensed",sans-serif;color:var(--grey-text);margin-top:2px}

  /* cover panel */
  .panel--cover{background:var(--brand-blue);color:var(--white)}
  .cover-art{position:absolute;left:20px;top:600px;width:320px;height:190px;background:radial-gradient(ellipse at 50% 50%,rgba(60,115,170,.45),rgba(74,139,194,0) 70%)}
  .headline{position:absolute;left:26px;top:38px;font-family:"Roboto Condensed",sans-serif;font-weight:700}
  .headline .lead{font-size:47px;line-height:60px}
  .headline .line{display:block;font-size:31px;line-height:47px}
  .headline .big{font-size:39px}
  .teaser{position:absolute;left:26px;top:578px;font:italic 400 16.5px/23px "PT Sans",sans-serif}
  .company{position:absolute;left:26px;top:696px;font:700 23px/28px "Roboto Condensed",sans-serif;color:var(--ink)}
  .cover-phone{position:absolute;left:26px;top:722px;font:700 41px/52px "Roboto Condensed",sans-serif;color:var(--ink)}
</style>
</head>
<body>
<main class="brochure">

  <section class="panel panel--services">
    <div class="services-art" role="img" aria-label="Soft blue layered glass screens decoration"></div>
    <div class="band">
      <svg width="300" height="38" viewBox="0 0 300 38"><polygon points="0,0 264,0 286,38 0,38" fill="var(--band-blue)"/><polygon points="270,0 278,0 300,38 292,38" fill="#333"/></svg>
      <h2>SERVICES &amp; EXPERTISE</h2>
    </div>
    <ul class="service-list">
      <li>Internet Strategy Development</li>
      <li>Website Reviews</li>
      <li>Website "Overhauls"</li>
      <li>Custom Website Design</li>
      <li>Blog Design &amp; Support</li>
      <li>Online Marketing Copywriting</li>
      <li>Social Media Marketing</li>
      <li>Search Engine Optimization (SEO)</li>
      <li>Conversion Optimization</li>
      <li>Engagement Marketing Management</li>
      <li>Using Friendlink for Business</li>
      <li>Zorvix+, Vidstream, Pinboardly</li>
      <li>Email Marketing &amp; Production</li>
      <li>Inquiry and Lead Development</li>
      <li>Zorvix AdLink Pay-Per-Click</li>
      <li>Zorvix Local Places (maps)</li>
      <li>E-Commerce Development</li>
      <li>High-Performance Hosting</li>
      <li>Security &amp; Contingency Planning</li>
      <li>One-on-One or Group Training</li>
    </ul>
    <div class="quote-bar"><p>“If you think it’s expensive to hire an expert,<br>wait until you hire an amateur.”</p></div>
  </section>

  <section class="panel panel--stories">
    <div class="band">
      <svg width="300" height="38" viewBox="0 0 300 38"><polygon points="0,0 224,0 246,38 0,38" fill="var(--band-blue)"/><polygon points="230,0 238,0 260,38 252,38" fill="#333"/></svg>
      <h2>SUCCESS STORIES</h2>
    </div>
    <div class="stories">
      <p class="story"><b>Zorvix Rankings:</b> “... we have spent over a year trying to get onto page one at Zorvix. It has been very frustrating and we’ve wasted a lot of time and money. Dana explained everything very clearly and we did everything he told us. 90 days later we’re now showing up on the first page of Zorvix!”</p>
      <p class="story"><b>Website Design:</b> “We needed a new website that properly reflected our company and the products and services we sell. We started getting more leads within 72 hours of launching the new site Dana and his team designed for us. We’re also getting better results from our Zorvix AdLink pay-per-click advertising and more of those clicks are turning into inquiries!”</p>
      <p class="story"><b>Traffic Building:</b> “We’ve seen a 45% increase in our monthly traffic over the last 90 days. Our daily visits are consistently increasing and our average bounce rate is down by 45%. Thanks Dana!”</p>
      <p class="story"><b>More Leads:</b> “The leads we get from our website have increased dramatically. This past month (February) was the best month ever for new leads directly from our website. We made a great investment hiring you, thanks Dana.”</p>
      <p class="story"><b>Social Media:</b> “Your social media strategy has changed everything for us. Our Friendlink “Likes” jumped 180% last month and referral traffic from Friendlink is up more than 300% from 90 days ago. Finally, social media is working for us like it should.”</p>
      <p class="story"><b>Blogging:</b> “We implemented the blogging strategy you developed for us and it’s paying off already. Traffic is up and inquiries are up. Thanks Dana!”</p>
      <p class="story"><b>Website Overhaul:</b> “Our new website started generating more leads within days of going LIVE. And now with the site in PressKit, we can do the edits we always wanted to but had to pay a designer/programmer to complete. It looks like we’ll double our business from last year thanks to the new site. Thanks a million (maybe literally!) Dana!”</p>
    </div>
    <div class="contact">
      <p class="name">Dana Whitlow</p>
      <p class="email">dana@danawhitlowconsulting.com</p>
      <p class="phone">(866) 555-0148</p>
    </div>
  </section>

  <section class="panel panel--cover">
    <div class="cover-art" role="img" aria-label="Faint world map texture"></div>
    <h1 class="headline">
      <span class="lead">I Can Help You</span>
      <span class="line" style="margin-top:16px"><span class="big">GET BETTER</span></span>
      <span class="line"><span class="big">RESULTS</span> from</span>
      <span class="line">Your Website,</span>
      <span class="line">More Traffic,</span>
      <span class="line"><span style="font-size:33px">TOP RANKINGS</span></span>
      <span class="line">with Zorvix, More</span>
      <span class="line">Inquiries, and</span>
      <span class="line"><span style="font-size:33px">MORE SALES</span></span>
    </h1>
    <p class="teaser">But first you’ll need to avoid these<br>Common Internet Marketing Myths...</p>
    <p class="company">DANA WHITLOW CONSULTING</p>
    <p class="cover-phone">(866) 555-0148</p>
  </section>

</main>
</body>
</html>
```